Boutique Wealth management firm needs a new business card design

I want to update my business card design to be more consistent with the look and feel of my website (www.brisvane-wealth.com). I would like to incorporate an ivory parchment background and am open to switching from the current "portrait" layout to a more traditional "landscape" orientation. The final design should convey stability and exclusivity and I want something in PDF format that is ready to send to the printer

Thank you all for taking the time to submit your designs for my project. I've made my decision and picked the design I like best. Thanks again!

```html
<!DOCTYPE html>
<html lang="en">
<head>
<meta charset="utf-8">
<title>Brisvane Wealth Advisory – Business Card</title>
<link rel="stylesheet" href="https://fonts.googleapis.com/css2?family=Cormorant+Garamond:wght@600&family=Arimo:wght@400&display=swap">
<style>
  :root {
    --page-bg: #d8d5cf;
    --ivory: #ecebe5;
    --maroon: #5b1a32;
    --card-text: #ffffff;
  }
  * { margin: 0; padding: 0; box-sizing: border-box; }
  html, body { width: 1200px; height: 960px; overflow: hidden; }
  body {
    background: var(--page-bg);
    display: flex;
    align-items: center;
    justify-content: center;
  }
  .business-card {
    width: 1000px;
    height: 572px;
    display: flex;
    box-shadow: 0 10px 30px rgba(0,0,0,0.18);
  }
  .brand-panel {
    width: 43%;
    background: var(--ivory);
    display: flex;
    align-items: center;
    justify-content: center;
  }
  .brand-name {
    font-family: "Cormorant Garamond", Georgia, serif;
    font-weight: 600;
    color: var(--maroon);
    text-align: center;
    line-height: 1;
  }
  .brand-name .primary { display: block; font-size: 72px; text-transform: uppercase; letter-spacing: 1px; }
  .brand-name .secondary { display: block; font-size: 34px; margin-top: 4px; }
  .contact-panel {
    width: 57%;
    background: var(--maroon);
    color: var(--card-text);
    padding: 64px 56px;
    font-family: Arimo, Arial, sans-serif;
  }
  .holder-name {
    font-family: "Cormorant Garamond", Georgia, serif;
    font-weight: 600;
    font-size: 34px;
    font-variant: small-caps;
    letter-spacing: 1px;
    line-height: 1;
  }
  .holder-name sup { font-size: 12px; }
  .holder-title {
    font-size: 22px;
    margin-top: 6px;
    padding-left: 30px;
  }
  .contact-list {
    list-style: none;
    margin-top: 44px;
  }
  .contact-list li {
    display: flex;
    align-items: flex-start;
    font-size: 21px;
    line-height: 1.25;
    margin-bottom: 16px;
  }
  .contact-list .icon {
    width: 22px;
    height: 22px;
    flex: none;
    margin-right: 22px;
    margin-top: 1px;
  }
  .license {
    font-size: 21px;
    margin-top: 10px;
    padding-left: 44px;
  }
</style>
</head>
<body>
  <article class="business-card">
    <section class="brand-panel">
      <h1 class="brand-name">
        <span class="primary">Brisvane</span>
        <span class="secondary">Wealth Advisory</span>
      </h1>
    </section>
    <section class="contact-panel">
      <h2 class="holder-name">Dale Corwin, CFP<sup>®</sup></h2>
      <p class="holder-title">Principal</p>
      <ul class="contact-list">
        <li>
          <svg class="icon" viewBox="0 0 24 24" aria-hidden="true"><path fill="#fff" d="M6.6 10.8a15.5 15.5 0 0 0 6.6 6.6l2.2-2.2c.3-.3.7-.4 1-.2 1.1.4 2.3.6 3.6.6.6 0 1 .4 1 1V20c0 .6-.4 1-1 1A17 17 0 0 1 3 4c0-.6.4-1 1-1h3.5c.6 0 1 .4 1 1 0 1.3.2 2.5.6 3.6.1.3 0 .7-.2 1z"/></svg>
          <span>925-555-0148</span>
        </li>
        <li>
          <svg class="icon" viewBox="0 0 24 24" aria-hidden="true"><rect x="2" y="5" width="20" height="14" rx="1.5" fill="#fff"/><path d="M3 6.5l9 6.5 9-6.5" fill="none" stroke="#5b1a32" stroke-width="1.6"/></svg>
          <span>Dale@brisvane-wealth.com</span>
        </li>
        <li>
          <svg class="icon" viewBox="0 0 24 24" aria-hidden="true"><circle cx="12" cy="12" r="10" fill="#fff"/><g fill="none" stroke="#5b1a32" stroke-width="1.4"><ellipse cx="12" cy="12" rx="4" ry="10"/><path d="M2 12h20M4 7h16M4 17h16"/></g></svg>
          <span>www.brisvane-wealth.com</span>
        </li>
        <li>
          <svg class="icon" viewBox="0 0 24 24" aria-hidden="true"><path fill="#fff" d="M12 2a7 7 0 0 0-7 7c0 5 7 13 7 13s7-8 7-13a7 7 0 0 0-7-7z"/><circle cx="12" cy="9" r="2.6" fill="#5b1a32"/></svg>
          <span>2870 Alder Creek Rd. #214<br>Harlow, CA 94570</span>
        </li>
      </ul>
      <p class="license">CA Insurance License #0K71863</p>
    </section>
  </article>
</body>
</html>
```